Help! We need PROFESSIONAL E-mail Signatures that POP!

9/12 UPDATE:
We have extended the deadline.
Also the logo we want used for Melsford has changed.

We have 8 employees working for three companies. We want our e-mail signatures to be the same format and cohesive, but each person has one company of the three that needs to be highlighted.
- Logos are attached and spreadsheet shows what information is needed for each employee as well as which of the logos should be the primary logo - first one displayed and slightly larger than the others.
- Please create one design first using the information for Daniel Wystan from Line 2 of the spreadsheet (provided three versions - Numbers, Excel, PDF
- All components need to be able to be changed or deleted.
- We need to be able to easily create new signatures for new employees
Updates

Need extra days to review

If you submitted a design prior to yesterday afternoon, please see original brief for the updated Melsford logo. This is the version of the Melsford logo that will be used for all the email signatures. The spreadsheet with the info for all 8 employees show different versions of this logo for different employees. Ignore that. Use this one logo in the design along with the Pelna and Brisk logos as indicated on the spreadsheet. Thanks!

Target Market(s)

New/existing clients!

Industry/Entity Type

Property development, commercial construction, property management

Font styles to use
Sans Serif

Requirements
Must have
• A lot of info with a clean look
Nice to have
• Consistency and cohesion
Should not have
• Too many elements - UPDATE: No photos - thanks!

```html
<!DOCTYPE html>
<html lang="en">
<head>
<meta charset="utf-8">
<title>Maren Holt – Email Signature</title>
<link href="https://fonts.googleapis.com/css2?family=Roboto+Condensed:wght@400;700&family=Roboto:wght@400;500;700&display=swap" rel="stylesheet">
<style>
  :root {
    --ink: #333333;
    --paper-shade: #ececec;
    --brisk-blue: #1f7ac2;
    --melsford-green: #5aaf34;
    --pelna-orange: #f26522;
    --panel: #474747;
    --panel-text: #ffffff;
    --rule: #bdbdbd;
    --panel-rule: #9a9a9a;
  }
  * { margin: 0; padding: 0; box-sizing: border-box; }
  html, body { width: 1200px; height: 300px; overflow: hidden; background: var(--paper-shade); }
  .signature { position: relative; width: 1200px; height: 300px; overflow: hidden; font-family: "Roboto", Arial, sans-serif; }

  .contact-panel { position: absolute; left: 600px; top: 0; width: 600px; height: 300px; background: var(--panel); color: var(--panel-text); }
  .accent-bar { position: absolute; left: 420px; top: 0; width: 286px; height: 27px; background: var(--brisk-blue); z-index: 1; }

  .identity-card { position: absolute; left: 0; top: 27px; width: 600px; height: 273px; z-index: 2;
    background: linear-gradient(135deg, #f1f1f1 0%, #ffffff 35%, #f4f4f4 60%, #ffffff 100%); }

  .name { position: absolute; left: 48px; top: 14px; font-family: "Roboto Condensed", Arial, sans-serif; font-weight: 700; font-size: 37px; letter-spacing: 0.3px; color: var(--ink); }
  .role { position: absolute; left: 48px; top: 58px; font-weight: 400; font-size: 30px; color: var(--brisk-blue); }
  .companies { position: absolute; left: 48px; top: 105px; font-weight: 500; font-size: 19px; color: var(--ink); white-space: nowrap; }
  .companies .brisk { color: var(--brisk-blue); }
  .companies .melsford { color: var(--melsford-green); }
  .companies .pelna { color: var(--pelna-orange); }
  .companies .sep { margin: 0 8px; }
  .divider { position: absolute; left: 48px; top: 144px; width: 477px; height: 1px; background: var(--rule); }

  .brand-row { position: absolute; left: 48px; top: 160px; width: 480px; height: 86px; display: flex; align-items: center; gap: 56px; }
  .brand { font-weight: 700; font-size: 26px; color: var(--ink); white-space: nowrap; }
  .brand--primary { font-size: 32px; }

  .contact-list { position: absolute; right: 52px; top: 21px; list-style: none; }
  .contact-list li { display: flex; justify-content: flex-end; align-items: center; gap: 12px; height: 29.5px;
    font-weight: 500; font-size: 19px; white-space: nowrap; }
  .contact-list svg { width: 17px; height: 17px; fill: var(--panel-text); flex: none; }

  .panel-rule { position: absolute; left: 48px; right: 30px; top: 203px; height: 1px; background: var(--panel-rule); }
  .notice { position: absolute; left: 44px; right: 30px; top: 211px; font-size: 9px; line-height: 13px; text-align: right; color: var(--panel-text); }
  .notice strong { font-weight: 700; }
</style>
</head>
<body>
<div class="signature">
  <section class="contact-panel">
    <ul class="contact-list">
      <li><svg viewBox="0 0 24 24"><path d="M7 1h10a2 2 0 0 1 2 2v18a2 2 0 0 1-2 2H7a2 2 0 0 1-2-2V3a2 2 0 0 1 2-2zm0 3v14h10V4zm5 15.5a1.3 1.3 0 1 0 0 2.6 1.3 1.3 0 0 0 0-2.6z"/></svg><span>555-014-2286</span></li>
      <li><svg viewBox="0 0 24 24"><path d="M6.6 10.8a15 15 0 0 0 6.6 6.6l2.2-2.2a1 1 0 0 1 1-.25 11.4 11.4 0 0 0 3.6.6 1 1 0 0 1 1 1V20a1 1 0 0 1-1 1A17 17 0 0 1 3 4a1 1 0 0 1 1-1h3.5a1 1 0 0 1 1 1c0 1.25.2 2.45.6 3.6a1 1 0 0 1-.25 1z"/></svg><span>Brisk Builders: 555-013-7740 x104</span></li>
      <li><svg viewBox="0 0 24 24"><path d="M2 4h20v16H2zm2 2v12h16V6zm2 2h5v5H6zm7 1h5v1.5h-5zm0 3h5v1.5h-5zM6 15h12v1.5H6z"/></svg><span>Chicago GC Lic#: TGC048391</span></li>
      <li><svg viewBox="0 0 24 24"><path d="M2 5h20v14H2zm2 2v.5l8 5 8-5V7zm0 2.8V17h16V9.8l-8 5z"/></svg><span>operations@melsford.com</span></li>
      <li><svg viewBox="0 0 24 24"><path d="M12 1a7 7 0 0 1 7 7c0 5.2-7 15-7 15S5 13.2 5 8a7 7 0 0 1 7-7zm0 4a3 3 0 1 0 0 6 3 3 0 0 0 0-6z"/></svg><span>48 N. Alder St., Ste 2A, Fairbrook IL 60599</span></li>
      <li><svg viewBox="0 0 24 24"><path d="M12 2a10 10 0 1 0 0 20 10 10 0 0 0 0-20zm6.9 6h-3a15 15 0 0 0-1.3-3.9A8 8 0 0 1 18.9 8zM12 4c.9 1.2 1.6 2.5 2 4h-4c.4-1.5 1.1-2.8 2-4zM4.3 14a8 8 0 0 1 0-4h3.4a16 16 0 0 0 0 4zm.8 2h3a15 15 0 0 0 1.3 3.9A8 8 0 0 1 5.1 16zm3-8h-3a8 8 0 0 1 4.3-3.9A15 15 0 0 0 8.1 8zM12 20c-.9-1.2-1.6-2.5-2-4h4c-.4 1.5-1.1 2.8-2 4zm2.3-6H9.7a14 14 0 0 1 0-4h4.6a14 14 0 0 1 0 4zm.3 5.9a15 15 0 0 0 1.3-3.9h3a8 8 0 0 1-4.3 3.9zm1.7-5.9a16 16 0 0 0 0-4h3.4a8 8 0 0 1 0 4z"/></svg><span>www.builtbrisk.com</span></li>
    </ul>
    <div class="panel-rule"></div>
    <p class="notice"><strong>CONFIDENTIALITY NOTICE:</strong> This e-mail is intended only for the recipient named and may contain confidential, privileged, and exempt from disclosure under applicable laws. If you are not the named recipient, you may have received this transmission in error. We ask that you, please immediately notify us by e-mail at operations@melsford.com and remove this and all attached file(s) from your system. You are notified that any disclosure, copying, distribution, or use of the information in this transmission if you are not the intended recipient is prohibited and may expose you to liability</p>
  </section>

  <div class="accent-bar"></div>

  <section class="identity-card">
    <h1 class="name">MAREN HOLT</h1>
    <p class="role">Operations Manager</p>
    <p class="companies"><span class="brisk">Brisk Builders</span><span class="sep">I</span><span class="melsford">Melsford</span><span class="sep">I</span><span class="pelna">Pelna Brokerage &amp; Management</span></p>
    <div class="divider"></div>
    <div class="brand-row">
      <span class="brand brand--primary">Brisk</span>
      <span class="brand">Melsford</span>
      <span class="brand">Pelna</span>
    </div>
  </section>
</div>
</body>
</html>
```